Postcard For neighbors near worksite

We are a residential interior and exterior painting company. I will be sending post cards out in neighborhoods that we will be currently working in. Basically giving the neighbors a "Neighborhood Notice" that we are in the area and would like to give a Free Estimate to anyone in that neighborhood. I will attach a file of another companies idea that I like. Also, I attached my Logo. Brightcoat Painting & More

Target Market(s)

Neighbors near where we are working

Industry/Entity Type

It Company

Requirements
Must have
• Website: Brightcoatpaint.example
• Number: 555.204.6617

```html
<!DOCTYPE html>
<html lang="en">
<head>
<meta charset="utf-8">
<title>Brightcoat Painting &amp; More – Neighborhood Notice Postcard</title>
<link href="https://fonts.googleapis.com/css2?family=Oswald:wght@300;400;600;700&family=Lato:wght@400;700;900&display=swap" rel="stylesheet">
<style>
  :root {
    --red: #ec1c24;
    --gray: #7a7a7a;
    --gray-dark: #6d6e70;
    --gray-light: #e6e7e8;
    --ink: #1a1a1a;
    --white: #ffffff;
    --page: #efefef;
  }
  * { margin: 0; padding: 0; box-sizing: border-box; }
  html, body { width: 1070px; height: 1200px; overflow: hidden; background: var(--page); }
  body { position: relative; font-family: "Lato", sans-serif; color: var(--ink); }

  .card {
    position: absolute; left: 35px; width: 1000px; height: 556px;
    background: var(--white); overflow: hidden;
    box-shadow: 0 3px 10px rgba(0,0,0,.25);
  }
  .card--front { top: 29px; }
  .card--back { top: 614px; }

  /* ---------- Front ---------- */
  .front-header {
    position: absolute; left: 0; top: 0; width: 100%; height: 116px;
    background: var(--red); color: var(--white);
    display: flex; align-items: center; justify-content: center;
    font-family: "Oswald", sans-serif; font-size: 76px; letter-spacing: 2px;
  }
  .front-header .light { font-weight: 300; margin-right: 24px; }
  .front-header .bold { font-weight: 700; }

  .front-photo {
    position: absolute; left: 0; top: 126px; width: 100%; height: 282px;
    background: linear-gradient(90deg, #9a9a9a 0%, #d6d6d6 35%, #bdbdbd 62%, #d9c7ae 78%, #b79f86 100%);
  }
  .front-photo-curves { position: absolute; left: 0; top: 126px; width: 1000px; height: 282px; }
  .front-band { position: absolute; left: 0; top: 408px; width: 100%; height: 10px; background: var(--gray); }

  .call-badge {
    position: absolute; left: 32px; top: 240px; width: 150px; height: 150px; border-radius: 50%;
    background: radial-gradient(circle at 40% 35%, #3a3a3a, #0d0d0d 70%);
    color: var(--white); font-family: "Oswald", sans-serif; font-weight: 400;
    display: flex; flex-direction: column; align-items: center; justify-content: center;
    line-height: 1.15; box-shadow: 0 2px 6px rgba(0,0,0,.4);
  }
  .call-badge .label { font-size: 21px; }
  .call-badge .number { font-size: 21px; }

  .brand-name {
    font-family: "Lato", sans-serif; font-weight: 900; color: var(--red);
    line-height: 1.05;
  }
  .front-brand { position: absolute; left: 32px; top: 440px; width: 240px; font-size: 29px; }

  .service-list {
    position: absolute; left: 285px; top: 448px; list-style: none;
    font-family: "Oswald", sans-serif; font-weight: 400; font-size: 25px; letter-spacing: 1px;
  }
  .service-list li { display: flex; align-items: center; gap: 12px; height: 40px; }
  .service-list svg { width: 20px; height: 20px; }

  .estimate-box { position: absolute; left: 609px; top: 398px; width: 374px; }
  .estimate-box .title {
    height: 87px; background: var(--red); color: var(--white);
    font-family: "Oswald", sans-serif; font-weight: 700; font-size: 38px; letter-spacing: 1.5px;
    display: flex; align-items: center; justify-content: center;
  }
  .estimate-box .sub {
    height: 49px; background: var(--gray); color: var(--white);
    font-size: 22px; display: flex; align-items: center; justify-content: center;
  }

  /* ---------- Back ---------- */
  .back-brand {
    position: absolute; left: 0; top: 0; width: 232px; height: 119px;
    display: flex; align-items: center; padding: 0 26px; font-size: 25px;
  }
  .back-tagline {
    position: absolute; left: 232px; top: 0; width: 330px; height: 119px;
    background: var(--red); color: var(--white);
    font-family: "Oswald", sans-serif; font-weight: 300; font-size: 22px; line-height: 1.1;
    display: flex; align-items: center; padding-left: 21px;
  }
  .interior-photo {
    position: absolute; left: 0; top: 131px; width: 276px; height: 170px;
    background: linear-gradient(180deg, #9a9c9a 0%, #7d7f7c 55%, #a07a55 80%, #5a4a3c 100%);
  }
  .interior-panel {
    position: absolute; left: 276px; top: 131px; width: 287px; height: 179px;
    background: var(--gray); color: var(--white); padding: 38px 24px 0 18px;
  }
  .section-title { font-family: "Oswald", sans-serif; font-weight: 300; font-size: 13px; text-transform: uppercase; margin-bottom: 12px; }
  .section-text { font-size: 12.5px; line-height: 1.38; text-align: justify; }
  .exterior-panel {
    position: absolute; left: 0; top: 310px; width: 563px; height: 113px;
    background: var(--gray-light); padding: 22px 27px 0;
  }
  .exterior-panel .section-text { text-align: left; }
  .estimate-cta {
    position: absolute; left: 0; top: 430px; width: 276px; height: 126px;
    background: var(--red); color: var(--white);
    display: flex; flex-direction: column; align-items: center; padding-top: 13px;
  }
  .estimate-cta .cta-title { font-family: "Oswald", sans-serif; font-weight: 600; font-size: 20px; letter-spacing: .5px; }
  .phone-pill {
    margin-top: 8px; width: 224px; height: 38px; border-radius: 19px;
    background: linear-gradient(#2a2a2a, #050505); border: 2px solid #f2f2f2;
    display: flex; align-items: center; justify-content: center; gap: 10px;
    font-family: "Oswald", sans-serif; font-weight: 600; font-size: 22px; letter-spacing: 1px;
  }
  .phone-pill svg { width: 20px; height: 20px; }
  .estimate-cta .web { margin-top: 8px; font-size: 13px; letter-spacing: .4px; }
  .crew-photo {
    position: absolute; left: 276px; top: 423px; width: 287px; height: 133px;
    background: linear-gradient(90deg, #8b8580 0%, #a06c55 45%, #b9a48c 75%, #8e8a84 100%);
  }
  .stamp-box { position: absolute; left: 866px; top: 25px; width: 117px; height: 84px; border: 1.5px solid #9a9a9a; }
  .address-line { position: absolute; left: 637px; width: 346px; height: 1.5px; background: #9a9a9a; }
</style>
</head>
<body>

<section class="card card--front" aria-label="Postcard front">
  <header class="front-header"><span class="light">NEIGHBORHOOD</span><span class="bold">NOTICE!!!</span></header>

  <div class="front-photo" role="img" aria-label="Two-storey stucco houses with tiled roofs, left half in black and white, right half in colour"></div>
  <svg class="front-photo-curves" viewBox="0 0 1000 282" aria-hidden="true">
    <path d="M580 282 C 700 200, 770 100, 790 0" fill="none" stroke="#fff" stroke-width="1.5"/>
    <path d="M740 282 C 840 230, 940 205, 1000 200" fill="none" stroke="#fff" stroke-width="1.5"/>
  </svg>
  <div class="front-band"></div>

  <div class="call-badge"><span class="label">CALL US:</span><span class="number">555-204-6617</span></div>

  <div class="brand-name front-brand">Brightcoat Painting &amp; More</div>

  <ul class="service-list">
    <li><svg viewBox="0 0 20 20" aria-hidden="true"><rect x="1.5" y="3" width="14" height="14" fill="none" stroke="#1a1a1a" stroke-width="2"/><path d="M5 9.5l4 4 9-10" fill="none" stroke="#1a1a1a" stroke-width="2.2"/></svg>Interior Painting</li>
    <li><svg viewBox="0 0 20 20" aria-hidden="true"><rect x="1.5" y="3" width="14" height="14" fill="none" stroke="#1a1a1a" stroke-width="2"/><path d="M5 9.5l4 4 9-10" fill="none" stroke="#1a1a1a" stroke-width="2.2"/></svg>Exterior Painting</li>
  </ul>

  <div class="estimate-box">
    <div class="title">FREE ESTIMATE!</div>
    <div class="sub">to anyone in neighborhood</div>
  </div>
</section>

<section class="card card--back" aria-label="Postcard back">
  <div class="brand-name back-brand">Brightcoat Painting &amp; More</div>
  <div class="back-tagline">Professional Residential and<br>Commercial Painting Services</div>

  <div class="interior-photo" role="img" aria-label="Freshly painted grey dining room with wooden table and chandelier"></div>
  <div class="interior-panel">
    <h2 class="section-title">Interior Painting</h2>
    <p class="section-text">Does the look of your home or apartment need revitalized? Let our painting contractors transform the look of your home’s interior.</p>
  </div>

  <div class="exterior-panel">
    <h2 class="section-title">Exterior Painting</h2>
    <p class="section-text">Add value and curb appeal to your home or business with our exterior painting services.<br>We do house painting and much more.</p>
  </div>

  <div class="estimate-cta">
    <div class="cta-title">Request Free Estimate!</div>
    <div class="phone-pill">
      <svg viewBox="0 0 20 20" aria-hidden="true"><circle cx="10" cy="10" r="8.5" fill="none" stroke="#fff" stroke-width="1.6"/><path d="M7 5.5l1.6 2.4-1 1.1c.6 1.3 1.5 2.2 2.8 2.8l1.1-1 2.4 1.6-.8 1.6c-3.6-.2-6.7-3.3-6.9-6.9z" fill="#fff"/></svg>
      555-204-6617
    </div>
    <div class="web">www.brightcoatpaint.example</div>
  </div>
  <div class="crew-photo" role="img" aria-label="Painting crew in white shirts standing in front of a freshly painted wall"></div>

  <div class="stamp-box" aria-label="Stamp area"></div>
  <div class="address-line" style="top:216px"></div>
  <div class="address-line" style="top:263px"></div>
  <div class="address-line" style="top:310px"></div>
</section>

</body>
</html>
```